Business Card Design Project

I need a business card design for a new business called Tolland Insurance Services. I am a small insurance broker that will provide business insurance services mostly to contractors and small businesses. My business is all about customer service and assistance rather than being a price driven/focused business. I want my business card to be professional giving the impression that I am larger than one person but not a corporate company. I have attached a copy of my logo.
Updates

Hi all

I have been advised that I need to show the following info for compliance reasons on my card. It only has to be small.

Can you please include either front or back:

Tolland Insurance Services Pty Ltd [ABN 61827405193] AR No 586714 as Authorised Representative of Brackford Insurance Group Pty Ltd ACN 274 906 518 ABN 82 274 906 518 AFS Licence No 718264

Reason: I need a further change to be made to the design. I need the contact number of 1300476815 added to the business card.

Hi All

I need one last change made to the card.

Can you please include the phone number 1300476815 to the card. If possible can this be made fairly clear on the card, either large on the back or another design idea you may have.

Target Market(s)

30+ Professionals

Industry/Entity Type

Insurance

Requirements
Must have
• I want a double sided design. My details to go on the card are as follows:

Dylan Tolland QRPSUV (Snr Assoc.) CIP
Director
PO Box 872, Kestrelvale SA 5091
Phone: 0438 617 204
Fax 08 8397 2418
Email: dylan@tollandinsure.example
Website: http://www.tollandinsure.example
Twitter: Tollandinsure
Facebook: facebook.com/tollandinsure

```html
<!DOCTYPE html>
<html lang="en">
<head>
<meta charset="utf-8">
<title>Tolland Insurance Services – Business Card</title>
<link rel="stylesheet" href="https://fonts.googleapis.com/css2?family=Arimo:ital,wght@0,400;0,700;1,400&display=swap">
<style>
  :root {
    --page-bg: #f3f3f3;
    --card-dark: #2b2a2a;
    --card-glow: #4a4949;
    --band-white: #ffffff;
    --brand-red: #e0222a;
    --ink-dark: #1f1f1f;
    --ink-light: #f4f4f4;
    --ink-muted: #5c5c5c;
  }
  * { margin: 0; padding: 0; box-sizing: border-box; }
  html, body { width: 900px; height: 1200px; overflow: hidden; }
  body {
    background: var(--page-bg);
    font-family: "Arimo", Arial, sans-serif;
    position: relative;
  }
  .card {
    position: absolute;
    left: 103px;
    width: 721px;
    height: 464px;
    background: radial-gradient(ellipse at 50% 45%, var(--card-glow) 0%, var(--card-dark) 70%);
    overflow: hidden;
  }
  .card--front { top: 70px; }
  .card--back { top: 620px; }

  /* Front */
  .brand-band {
    position: absolute;
    left: 0; top: 148px;
    width: 100%; height: 169px;
    background: var(--band-white);
    display: flex;
    align-items: center;
    padding-left: 52px;
    gap: 22px;
  }
  .brand-dot {
    width: 26px; height: 26px;
    border-radius: 50%;
    background: var(--brand-red);
    flex: none;
  }
  .brand-name {
    font-weight: 400;
    color: var(--ink-dark);
    letter-spacing: 0.5px;
  }
  .brand-band .brand-name { font-size: 54px; }
  .compliance {
    position: absolute;
    left: 0; top: 376px;
    width: 100%;
    text-align: center;
    font-style: italic;
    font-size: 13px;
    line-height: 17.5px;
    color: var(--ink-muted);
  }

  /* Back */
  .back-accent {
    position: absolute;
    left: 332px; top: 48px;
    width: 58px; height: 58px;
    border-radius: 50%;
    background: var(--brand-red);
    opacity: 0.35;
  }
  .back-divider {
    position: absolute;
    left: 361px; top: 70px;
    width: 2px; height: 345px;
    background: linear-gradient(to bottom, rgba(255,255,255,0) 0%, rgba(255,255,255,0.85) 35%, rgba(255,255,255,0.6) 70%, rgba(255,255,255,0) 100%);
  }
  .back-brand {
    position: absolute;
    left: 12px; top: 212px;
    display: flex;
    align-items: center;
    gap: 12px;
  }
  .back-brand .brand-dot { width: 14px; height: 14px; }
  .back-brand .brand-name { font-size: 26px; color: #1a1a1a; }
  .holder {
    position: absolute;
    left: 372px; top: 120px;
    color: var(--ink-light);
    font-weight: 700;
    font-size: 17px;
    line-height: 23px;
  }
  .contact-list {
    position: absolute;
    left: 375px; top: 196px;
    list-style: none;
    color: var(--brand-red);
    font-weight: 700;
    font-size: 13.5px;
  }
  .contact-list li { height: 28.5px; }
  .contact-list li:nth-child(n+6) { height: 26.5px; }
</style>
</head>
<body>
  <section class="card card--front">
    <div class="brand-band">
      <span class="brand-dot"></span>
      <span class="brand-name">tolland insurance</span>
    </div>
    <p class="compliance">
      Tolland Insurance Services Pty Ltd [ABN 61827405193] AR No 586714<br>
      as Authorised Representative of Brackford Insurance Group Pty Ltd<br>
      ACN 274 906 518 ABN 82 274 906 518 AFS Licence No 718264
    </p>
  </section>

  <section class="card card--back">
    <span class="back-accent"></span>
    <span class="back-divider"></span>
    <div class="back-brand">
      <span class="brand-dot"></span>
      <span class="brand-name">tolland insurance</span>
    </div>
    <p class="holder">Dylan Tolland QRPSUV (Snr Assoc.) CIP<br>Director</p>
    <ul class="contact-list">
      <li>PO Box 872, Kestrelvale SA 5091</li>
      <li>Phone: 0438 617 204</li>
      <li>Fax 08 8397 2418</li>
      <li>Email: dylan@tollandinsure.example</li>
      <li>Website: http://www.tollandinsure.example</li>
      <li>Twitter: Tollandinsure</li>
      <li>Facebook: facebook.com/tollandinsure</li>
    </ul>
  </section>
</body>
</html>
```